We need a postcard design for a new promotion. We are an Australian online store that sells craft mosaic supplies, mainly tiles. View our website to understand more about our product range, www.brightlanecrafts.com.au and what we are about.

This promotion is designed to be used with mosaic studios / classes, as a referral system. They will give these cards to their students who will use them when placing an order. They will enter the studios / classes name during the checkout process. The studio will then receive a credit which will entitle them to receive mosaic supplies.

Target Market(s)

Women aged between 30-65, interest in art & craft

Industry/Entity Type

Store

Requirements
Must have
• Logo
Phone number: 1300 684 157
Website URL: www.brightlanecrafts.com.au

The following wording:

You Can Help Stock Your Studio...
Simply place any order with The Pebblecraft Depot and we will give your studio mosaic supplies, to the value of 10% of your purchase.

Just enter your studios name in the comments box during checkout to ensure your studio receives their supplies.

Studio Name:

```html
<!DOCTYPE html>
<html lang="en">
<head>
<meta charset="utf-8">
<title>The Pebblecraft Depot – Studio Referral Postcard</title>
<link rel="stylesheet" href="https://fonts.googleapis.com/css2?family=Open+Sans:wght@400;600;700&family=Montserrat:wght@400;600&display=swap">
<style>
  :root {
    --page: #e9e9ea;
    --card: #ffffff;
    --ink: #5a5a5e;
    --pink: #e2337c;
    --slate: #6a6fb0;
    --orange: #f39a26;
    --green: #8dc63f;
    --photo-warm: #c9b79a;
    --photo-deep: #6d7f72;
  }
  * { box-sizing: border-box; margin: 0; padding: 0; }
  html, body { width: 855px; height: 1200px; overflow: hidden; }
  body {
    background: var(--page);
    font-family: "Open Sans", Arial, sans-serif;
    position: relative;
  }
  .card {
    position: absolute;
    left: 120px;
    width: 615px;
    height: 490px;
    background: var(--card);
    overflow: hidden;
    box-shadow: 0 4px 14px rgba(0,0,0,.25);
  }
  .card--front { top: 51px; }
  .card--back { top: 580px; }

  /* front */
  .photo { position: absolute; left: 0; width: 100%; }
  .photo--tiles-top {
    top: 0; height: 163px;
    background: linear-gradient(100deg, #d9d2c4 0%, #c8a64a 25%, #7fa35a 45%, #3f7b4e 65%, #b7b0a2 100%);
  }
  .photo--tools {
    top: 291px; height: 199px;
    background: linear-gradient(100deg, #2d2d30 0%, #7a6f60 30%, #c7c2b8 55%, #4f86b5 75%, #c94b3c 100%);
  }
  .brand-strip {
    position: absolute; top: 163px; left: 0; width: 100%; height: 128px;
    display: flex; align-items: center; justify-content: space-between;
    padding: 0 40px 0 60px;
  }
  .brand { display: flex; align-items: center; gap: 12px; }
  .brand__mark { width: 30px; height: 30px; background: var(--pink); }
  .brand__name {
    font-family: "Montserrat", Arial, sans-serif;
    font-weight: 600; font-size: 22px; color: var(--ink);
    line-height: 1.1; text-transform: uppercase; letter-spacing: 1px;
  }
  .contact { text-align: right; color: var(--pink); }
  .contact__phone { font-family: "Montserrat", Arial, sans-serif; font-size: 40px; font-weight: 400; line-height: 1; }
  .contact__web { font-size: 15px; margin-top: 6px; }

  /* back */
  .back-brand { position: absolute; top: 30px; left: 40px; }
  .back-brand .brand__name { font-size: 18px; }
  .back-brand .brand__mark { width: 26px; height: 26px; }
  .photo--tile-fan {
    top: 0; left: 250px; width: 365px; height: 170px;
    clip-path: polygon(35% 0, 100% 0, 100% 100%, 0 100%);
    background: linear-gradient(135deg, #f2c14a 0%, #8dc63f 30%, #3bb7c8 55%, #e2337c 80%, #f39a26 100%);
  }
  .band { position: absolute; left: 0; width: 100%; color: #fff; }
  .band--heading {
    top: 170px; height: 58px; background: var(--slate);
    display: flex; align-items: center; padding-left: 30px;
  }
  .band--heading h1 { font-size: 32px; font-weight: 700; }
  .band--offer { top: 228px; height: 52px; background: var(--orange); padding: 9px 30px; font-size: 13px; line-height: 1.35; }
  .band--checkout { top: 280px; height: 52px; background: var(--green); padding: 9px 30px; font-size: 13px; line-height: 1.35; }
  .edge-strip {
    position: absolute; bottom: 0; left: 0; width: 100%; height: 14px;
    background: linear-gradient(90deg, #e2337c, #f39a26, #f2c14a, #8dc63f, #3bb7c8, #6a6fb0);
  }
</style>
</head>
<body>
  <section class="card card--front" aria-label="Postcard front">
    <div class="photo photo--tiles-top" role="img" aria-label="Photograph of colourful glass mosaic tiles and a tile nipper"></div>
    <div class="brand-strip">
      <div class="brand">
        <span class="brand__mark"></span>
        <span class="brand__name">The Pebblecraft<br>Depot</span>
      </div>
      <div class="contact">
        <div class="contact__phone">1300 684 157</div>
        <div class="contact__web">www.brightlanecrafts.com.au</div>
      </div>
    </div>
    <div class="photo photo--tools" role="img" aria-label="Photograph of mosaic tools, a wooden tile holder and coloured glass pebbles"></div>
  </section>

  <section class="card card--back" aria-label="Postcard back">
    <div class="brand back-brand">
      <span class="brand__mark"></span>
      <span class="brand__name">The Pebblecraft<br>Depot</span>
    </div>
    <div class="photo photo--tile-fan" role="img" aria-label="Photograph of rows of bright mosaic tiles in rainbow colours"></div>
    <div class="band band--heading"><h1>You Can Help Stock Your Studio...</h1></div>
    <p class="band band--offer">Simply place any order with The Pebblecraft Depot and we will give your studio mosaic supplies, to the value of 10% of your purchase.</p>
    <p class="band band--checkout">Just enter your studios name in the comments box during checkout to ensure your studio receives their supplies.</p>
    <div class="edge-strip"></div>
  </section>
</body>
</html>
```